PDBA website design

We need a page template website design for a cms website. Please see the brief attached for the details.
The client is the Pacific Downhorn Breeders Association which is an organisation promoting the White Suffolk Sheep Breed within Australia.

Reason: So that my top few designs can make changes and re-submit.

Target Market(s)

See attached brief

```html
<!DOCTYPE html>
<html lang="en">
<head>
<meta charset="utf-8">
<title>Pacific Downhorn Breeders Association</title>
<link href="https://fonts.googleapis.com/css2?family=Arimo:ital,wght@0,400;0,700;1,400&display=swap" rel="stylesheet">
<style>
:root{
  --green:#135e3f;
  --green-dark:#0f4f35;
  --yellow:#ecc930;
  --yellow-soft:#e8cf55;
  --red:#b5121b;
  --text:#2a2a2a;
  --footer:#2b2b2b;
  --footer-text:#c9c9c9;
  --btn-top:#fbfbfb;
  --btn-bottom:#e6e6e6;
}
*{box-sizing:border-box;margin:0;padding:0}
html,body{width:1108px;height:1200px;overflow:hidden;background:#fff}
body{font-family:"Arimo",Arial,sans-serif;color:var(--text);position:relative}
.header{position:absolute;left:0;top:0;width:1108px;height:137px}
.brand{position:absolute;left:93px;top:20px;height:100px;display:flex;align-items:center;gap:22px}
.brand-mark{width:96px;height:96px;border-radius:50%;background:var(--yellow);flex:none}
.brand-name{font-size:27px;font-weight:700;color:var(--green);line-height:1.1}
.tagline{font-size:18px;font-style:italic;color:var(--red);margin-top:10px}
.social{position:absolute;left:865px;top:47px;width:152px;height:47px;border:2px solid #1f3f8a;border-radius:3px;display:flex;align-items:center;gap:8px;padding-left:10px}
.social-square{width:28px;height:28px;background:#1f3f8a;flex:none}
.social-text{font-size:12px;font-weight:700;color:#1f3f8a;line-height:1.2}
.social-text strong{font-size:16px;display:block}
.nav{position:absolute;left:0;top:137px;width:1108px;height:46px;background:var(--green)}
.nav ul{list-style:none;display:flex;position:absolute;left:82px;top:0;height:46px}
.nav li{height:46px;display:flex;align-items:center;padding:0 21px;color:#fff;font-weight:700;font-size:14.5px;border-left:1px solid #2f7857;position:relative}
.nav li:first-child{border-left:none}
.nav li.active{color:var(--yellow)}
.nav li.active::after{content:"";position:absolute;left:50%;bottom:0;margin-left:-6px;border:6px solid transparent;border-bottom-color:var(--yellow)}
.dropdown{position:absolute;left:168px;top:184px;width:151px;background:var(--yellow-soft);padding:6px;z-index:2}
.dropdown div{height:27px;display:flex;align-items:center;padding-left:14px;font-size:13.5px;color:#222}
.dropdown .current{background:var(--green);color:#fff;margin-top:4px}
.hero{position:absolute;left:93px;top:187px;width:923px;height:335px;background:linear-gradient(180deg,#7d7a7a 0%,#8f8a80 30%,#d8c9a8 55%,#c99a6a 75%,#b45524 88%,#9a3f18 100%)}
.content{position:absolute;left:93px;top:547px;width:630px}
.content h1{font-size:25px;color:var(--green);font-weight:700}
.content h2{font-size:15px;font-weight:700;margin:12px 0 14px;color:#222}
.content p{font-size:12.6px;line-height:18.5px;margin-bottom:16px;color:#333}
.content a{color:var(--green);text-decoration:underline}
.side{position:absolute;left:760px;top:550px;width:257px}
.side-btn{height:53px;margin-bottom:16px;background:linear-gradient(180deg,var(--btn-top),var(--btn-bottom));border:1px solid #d6d6d6;display:flex;align-items:center;gap:12px;padding-left:14px;font-weight:700;font-size:14px;letter-spacing:.5px;color:#333;line-height:20px}
.side-btn svg{flex:none}
.side h3{font-size:22px;color:var(--green);font-weight:700;margin:14px 0 14px}
.sponsor{width:244px;height:190px;background:var(--yellow);display:flex;flex-direction:column}
.sponsor-name{height:50px;padding:8px 10px;color:var(--green);font-size:13px;line-height:1.2}
.sponsor-name strong{font-size:16px;display:block}
.sponsor-photo{height:115px;background:linear-gradient(180deg,#6b7a55,#cfc7b4 45%,#4f8a2a)}
.sponsor-url{flex:1;display:flex;align-items:center;padding-left:10px;font-weight:700;font-size:13px;color:var(--green);letter-spacing:.5px}
.footer{position:absolute;left:0;top:1115px;width:1108px;height:85px;background:var(--footer);color:var(--footer-text);font-size:12.5px;line-height:20px}
.footer-left{position:absolute;left:109px;top:24px}
.footer-right{position:absolute;right:82px;top:24px}
.footer a{color:var(--footer-text);text-decoration:underline}
</style>
</head>
<body>
<header class="header">
  <div class="brand">
    <span class="brand-mark"></span>
    <div>
      <div class="brand-name">Pacific Downhorn Breeders Association</div>
      <div class="tagline">Bred for Tomorrow</div>
    </div>
  </div>
  <div class="social"><span class="social-square"></span><div class="social-text">Find us on:<strong>Flockbook</strong></div></div>
</header>
<nav class="nav">
  <ul>
    <li>Home</li><li class="active">About</li><li>Search</li><li>Member Services</li><li>Stud</li><li>Pages</li><li>News</li><li>Sales</li><li>Links</li><li>Contact</li>
  </ul>
</nav>
<div class="dropdown"><div>Breed</div><div class="current">Genetic Testing</div></div>
<div class="hero" role="img" aria-label="Photo of a flock of white sheep standing on red soil before wooded hills"></div>
<main class="content">
  <h1>Welcome to PDBA</h1>
  <h2>Lorem Ipsum is simply dummy of the printing and typesetting industry.</h2>
  <p>Contrary to popular belief, Lorem Ipsum is not <a>simply random text</a>. It has roots in a piece of classical Latin literature from 45 BC, making it over 2000 years old. Henry Calloway, a Latin professor text of the printing and typesetting industry. Lorem Ipsum has been the industry's standard dummy text ever since the 1500s, when an unknown text of the printing and typesetting industry. Lorem Ipsum has been the industry's standard dummy text ever since the 1500s.</p>
  <p>when an unknown printer took a galley of type and scrambled it to <a>make a type specimen</a> book. It has survived not only five centuries, but also the leap into electronic typesetting, remaining unchanged text of the printing and typesetting industry.</p>
  <p>Contrary to popular belief, Lorem Ipsum is not <a>simply random text</a>. It has roots in a piece of classical Latin literature from 45 BC, making it over 2000 years old. Henry Calloway, a</p>
  <p>Latin professor text of the printing and typesetting industry. Lorem Ipsum has been the industry's standard dummy text ever since the 1500s, when an unknown text of the printing and typesetting industry. Lorem Ipsum has been the industry's standard dummy text ever since the 1500s.</p>
  <p>when an unknown printer took a galley of type and scrambled it to <a>make a type specimen</a> book. It has survived not only five centuries, but also the leap into electronic typesetting, remaining unchanged text of the printing and typesetting industry.</p>
  <p>Contrary to popular belief, Lorem Ipsum is not <a>simply random text</a>. It has roots in a piece of classical Latin literature from 45 BC, making it over 2000 years old. Henry Calloway, a</p>
</main>
<aside class="side">
  <div class="side-btn">
    <svg width="30" height="34" viewBox="0 0 30 34"><circle cx="15" cy="13" r="11" fill="none" stroke="#2a8a3a" stroke-width="2.5"/><circle cx="15" cy="13" r="6" fill="#2a8a3a"/><rect x="10" y="26" width="10" height="3" fill="#2a8a3a"/><rect x="11" y="30" width="8" height="3" fill="#2a8a3a"/></svg>
    Prime Lamb Helpline</div>
  <div class="side-btn">
    <svg width="30" height="28" viewBox="0 0 30 28"><rect x="1" y="4" width="28" height="23" fill="#2a8a3a"/><rect x="4" y="10" width="22" height="14" fill="#fff"/><g fill="#2a8a3a"><rect x="6" y="12" width="4" height="3"/><rect x="13" y="12" width="4" height="3"/><rect x="20" y="12" width="4" height="3"/><rect x="6" y="18" width="4" height="3"/><rect x="13" y="18" width="4" height="3"/><rect x="20" y="18" width="4" height="3"/><rect x="7" y="0" width="3" height="6"/><rect x="20" y="0" width="3" height="6"/></g></svg>
    Events</div>
  <div class="side-btn">
    <svg width="32" height="32" viewBox="0 0 32 32"><circle cx="13" cy="9" r="7" fill="#2a8a3a"/><path d="M0 32c0-9 6-14 13-14s13 5 13 14z" fill="#2a8a3a"/><path d="M26 16v8M22 20h8" stroke="#2a8a3a" stroke-width="2.5"/></svg>
    Members Resources &amp;<br>WebManager Login</div>
  <div class="side-btn">
    <svg width="34" height="28" viewBox="0 0 34 28"><rect x="1" y="1" width="32" height="26" fill="none" stroke="#2a8a3a" stroke-width="2.5"/><rect x="6" y="6" width="10" height="9" fill="#2a8a3a"/><path d="M19 7h10M19 11h10M19 15h10M6 19h23M6 23h23" stroke="#2a8a3a" stroke-width="2"/></svg>
    Latest News</div>
  <h3>Sponsors</h3>
  <div class="sponsor">
    <div class="sponsor-name">Pacific Downhorn<strong>Breeders Association</strong></div>
    <div class="sponsor-photo" role="img" aria-label="Photo of white sheep grazing on green pasture"></div>
    <div class="sponsor-url">www.downhornbreeders.org</div>
  </div>
</aside>
<footer class="footer">
  <div class="footer-left">Address: PO Box 412, Fernvale, SA 5099<br>Phone :08 5550 14720 &nbsp; | &nbsp; Fax: 08 5550 1938 &nbsp; | &nbsp; Email info@downhornbreeders.org</div>
  <div class="footer-right">Copyright Pacific Downhorn Breeders Association<br>Website design and development by <a>Brightwork</a></div>
</footer>
</body>
</html>
```